Biz Card for Harrowfield Property Partners - HWPP

Harrowfield Property Partners is a commercial real estate acquisitions firm. We buy commercial property and need to raise capital from investors for each deal we buy. The vibe needs to be: give us your money, we will multiply it.
Our website: www.hrwpp-example.com
Competitors are: https://velmarholdings-example.com/, https://tribanquepartners-example.com/, http://www.ostrellecapital-example.com/
Target Market(s)
High Net Worth Individuals, Bankers, Insurance Companies, Commercial Real Estate Brokers.
Industry/Entity Type
Investment Banking
Contact Information for Business Card
Name, Title, Addess, Cell#, Office#, email, website
Requirements
Must have
- use one of our logos. See website for look and feel: www.hrwpp-example.com
Nice to have
- see website: www.hrwpp-example.com

```html
<!DOCTYPE html>
<html lang="en">
<head>
<meta charset="utf-8">
<title>Harrowfield Property Partners – Business Card</title>
<link href="https://fonts.googleapis.com/css2?family=Lato:wght@400;700&display=swap" rel="stylesheet">
<style>
  :root {
    --backdrop: #5a5c60;
    --card-navy: #0b2640;
    --ink-white: #ffffff;
    --ink-muted: #8e9bab;
    --divider: #b9c2cc;
  }
  * { box-sizing: border-box; margin: 0; padding: 0; }
  html, body {
    width: 1200px; height: 1000px; overflow: hidden;
    background: var(--backdrop);
    font-family: "Lato", sans-serif;
  }
  .canvas { position: relative; width: 1200px; height: 1000px; }
  .card {
    position: absolute;
    width: 620px; height: 370px;
    background: var(--card-navy);
    border-radius: 26px;
    box-shadow: 0 18px 40px rgba(0,0,0,0.35);
    color: var(--ink-white);
  }
  .card--front { left: 80px; top: 90px; }
  .card--back { left: 500px; top: 530px; }

  .brand-mark {
    display: block;
    border-radius: 50%;
    background: var(--ink-white);
  }
  .brand-name {
    font-weight: 700;
    color: var(--ink-white);
    letter-spacing: 0.12em;
    text-transform: uppercase;
    line-height: 1.15;
  }

  /* Front */
  .front-lockup {
    position: absolute; left: 0; right: 0; top: 70px;
    display: flex; flex-direction: column; align-items: center; gap: 26px;
  }
  .front-lockup .brand-mark { width: 130px; height: 130px; }
  .front-lockup .brand-name { font-size: 30px; text-align: center; }

  /* Back */
  .back-lockup {
    position: absolute; left: 40px; top: 40px;
    display: flex; align-items: center; gap: 22px;
  }
  .back-lockup .brand-mark { width: 110px; height: 110px; }
  .back-lockup .brand-name { font-size: 22px; width: 380px; }

  .identity {
    position: absolute; right: 330px; top: 190px;
    text-align: right;
  }
  .identity__name { font-size: 25px; font-weight: 700; }
  .identity__title { font-size: 15px; color: var(--ink-muted); margin-top: 2px; }
  .identity__address { font-size: 14px; margin-top: 18px; line-height: 1.35; }

  .divider {
    position: absolute; left: 305px; top: 190px;
    width: 1px; height: 100px; background: var(--divider);
  }

  .contact-list {
    position: absolute; left: 325px; top: 188px;
    list-style: none;
    font-size: 15px; color: var(--ink-muted);
  }
  .contact-list li { display: flex; align-items: center; gap: 10px; height: 26px; }
  .contact-list svg { width: 13px; height: 13px; fill: var(--ink-white); flex: none; }
</style>
</head>
<body>
<main class="canvas">
  <section class="card card--front" aria-label="Card front">
    <div class="front-lockup">
      <span class="brand-mark" aria-hidden="true"></span>
      <p class="brand-name">Harrowfield Property Partners</p>
    </div>
  </section>

  <section class="card card--back" aria-label="Card back">
    <div class="back-lockup">
      <span class="brand-mark" aria-hidden="true"></span>
      <p class="brand-name">Harrowfield Property Partners</p>
    </div>

    <div class="identity">
      <p class="identity__name">Daniel Moravec</p>
      <p class="identity__title">Founder/CEO</p>
      <p class="identity__address">480 Linden Crest Ave, Suite 910<br>Marlow Springs, FL 33290</p>
    </div>

    <span class="divider" aria-hidden="true"></span>

    <ul class="contact-list">
      <li>
        <svg viewBox="0 0 16 16" aria-hidden="true"><path d="M3.6 1.2l2.3 2.6-1.3 1.8c.9 2 2.5 3.7 4.6 4.7l1.8-1.3 2.6 2.3-1.3 2.4C6.9 13.5 2.5 9.1 1.3 3z"/></svg>
        (555) 214-0637
      </li>
      <li>
        <svg viewBox="0 0 16 16" aria-hidden="true"><path d="M1 5c2-3 12-3 14 0l-1 2.2-3-.6V5H5v1.6l-3 .6zM3 9h10l1 5H2zm5 1.5a1.6 1.6 0 100 3.2 1.6 1.6 0 000-3.2z"/></svg>
        (555) 214-0638
      </li>
      <li>
        <svg viewBox="0 0 16 16" aria-hidden="true"><path d="M1 3h14v10H1zm1.5 1.4v.3L8 8.6l5.5-3.9v-.3zM2.5 6.4v5.1h11V6.4L8 10.3z"/></svg>
        dmoravec@hrwpp-example.com
      </li>
      <li>
        <svg viewBox="0 0 16 16" aria-hidden="true"><path d="M8 1a7 7 0 100 14A7 7 0 008 1zm0 1.4c.8.8 1.5 2.3 1.7 4.1H6.3C6.5 4.7 7.2 3.2 8 2.4zM2.5 7.5h2.4c.1 1.9.6 3.5 1.3 4.7a5.6 5.6 0 01-3.7-4.7zm0-1a5.6 5.6 0 013.7-4.7c-.7 1.2-1.2 2.8-1.3 4.7zm3.8 1h3.4c-.2 1.8-.9 3.3-1.7 4.1-.8-.8-1.5-2.3-1.7-4.1zm4.8 0h2.4a5.6 5.6 0 01-3.7 4.7c.7-1.2 1.2-2.8 1.3-4.7zm0-1c-.1-1.9-.6-3.5-1.3-4.7a5.6 5.6 0 013.7 4.7z"/></svg>
        www.hrwpp-example.com
      </li>
    </ul>
  </section>
</main>
</body>
</html>
```